Varnok Development and Management Corp. Business Card

A logo design project has been started for our Calgary-Alberta, Canada based land development and project management company. Using this logo, a clean, sleek, professional business card is to be developed (for digital or print media) representing the principals of the company (community, sustainability, and harmony).
Updates

Project Deadline Extended
Reason: Logo design recently completed.

Adobe Illustrator Vector file uploaded. Thanks, Lew

Target Market(s)

Similar business development professionals and other engineering project management personnel involved in land developemtn. Also used to as as the brand and image with both private individuals (Landowners), public officials (policy makers), and investors (banks, venture capitalists).

Industry/Entity Type

Digital

Requirements
Must have
• Open to designers opinion. Based on logo. Must have logo, and space for employee name, title, address, website, office / cell numbers.
Should not have
• No Palm trees or tropical references. Company is based in Calgary, Alberta, Canada.

```html
<!DOCTYPE html>
<html lang="en">
<head>
<meta charset="utf-8">
<title>Varnok Development and Management Corp. Business Card</title>
<link rel="stylesheet" href="https://fonts.googleapis.com/css2?family=Open+Sans:wght@400;600&display=swap">
<style>
  :root {
    --stage: #3b3b3b;
    --card-dark: #0d0f10;
    --card-dark-edge: #1c1f21;
    --paper: #ffffff;
    --green: #a4c23a;
    --ink: #1a1a1a;
    --muted: #8a8a8a;
    --rule: #7a7a7a;
    --band: #0b0b0b;
    --band-top: #4a4a4a;
    --white: #ffffff;
  }
  * { margin: 0; padding: 0; box-sizing: border-box; }
  html, body { width: 1200px; height: 750px; overflow: hidden; }
  body {
    background: var(--stage);
    font-family: "Open Sans", Arial, sans-serif;
    position: relative;
  }
  .card {
    position: absolute;
    top: 211px;
    width: 511px;
    height: 292px;
    border-radius: 24px;
    overflow: hidden;
  }
  /* Front */
  .card-front {
    left: 78px;
    background: radial-gradient(ellipse at 50% 45%, var(--card-dark-edge) 0%, var(--card-dark) 75%);
  }
  .front-brand {
    position: absolute;
    left: 0; right: 0; top: 112px;
    text-align: center;
    color: var(--green);
    font-weight: 600;
  }
  .front-brand .brand-name { display: block; font-size: 54px; letter-spacing: 3px; line-height: 1; }
  .front-brand .brand-tag { display: block; font-size: 14px; margin-top: 8px; letter-spacing: 0.2px; }

  /* Back */
  .card-back {
    left: 609px;
    background: var(--paper);
  }
  .back-brand {
    position: absolute;
    left: 30px; width: 196px; top: 132px;
    text-align: center;
    color: var(--green);
    font-weight: 600;
  }
  .back-brand .brand-name { display: block; font-size: 28px; letter-spacing: 1.5px; line-height: 1; }
  .back-brand .brand-tag { display: block; font-size: 8px; margin-top: 4px; }
  .divider {
    position: absolute;
    left: 246px; top: 68px;
    width: 2px; height: 113px;
    background: var(--rule);
  }
  .contact-list {
    position: absolute;
    left: 277px; top: 66px;
    list-style: none;
    font-size: 14px;
    color: var(--ink);
    line-height: 1.3;
  }
  .contact-list li { display: flex; align-items: flex-start; }
  .contact-list li + li { margin-top: 1px; }
  .contact-list svg { width: 12px; height: 12px; margin-top: 3px; margin-right: 9px; flex: none; fill: var(--green); }
  .contact-list .address { color: var(--green); margin-bottom: 6px; }

  .name-band {
    position: absolute;
    left: 0; right: 0; bottom: 0;
    height: 79px;
    background: var(--band);
    border-top: 5px solid var(--band-top);
  }
  .name-band::after {
    content: "";
    position: absolute;
    left: 0; right: 0; bottom: 0;
    height: 4px;
    background: var(--green);
  }
  .person {
    position: absolute;
    left: 0; width: 544px; top: 10px;
    text-align: center;
    color: var(--white);
  }
  .person-name { font-size: 20px; line-height: 1.1; }
  .person-title { font-size: 14px; margin-top: 1px; }
</style>
</head>
<body>
  <section class="card card-front" aria-label="Card front">
    <div class="front-brand">
      <span class="brand-name">VARNOK</span>
      <span class="brand-tag">Development and Management Corp</span>
    </div>
  </section>

  <section class="card card-back" aria-label="Card back">
    <div class="back-brand">
      <span class="brand-name">VARNOK</span>
      <span class="brand-tag">Development and Management Corp</span>
    </div>
    <div class="divider"></div>
    <ul class="contact-list">
      <li class="address">
        <svg viewBox="0 0 12 12"><path d="M6 0a4 4 0 0 0-4 4c0 3 4 8 4 8s4-5 4-8a4 4 0 0 0-4-4zm0 5.5A1.5 1.5 0 1 1 6 2.5a1.5 1.5 0 0 1 0 3z"/></svg>
        <span>address (street address<br>suite number, city, state, zip</span>
      </li>
      <li>
        <svg viewBox="0 0 12 12"><path d="M1 4c0-2 10-2 10 0v1H8V4H4v1H1zM2 6h8l1 4H1z"/></svg>
        <span>0123 456 789</span>
      </li>
      <li>
        <svg viewBox="0 0 12 12"><path d="M3 0h6v12H3zm1 1v9h4V1z"/></svg>
        <span>0123 456 789</span>
      </li>
      <li>
        <svg viewBox="0 0 12 12"><path d="M1 2h10v8H1zm1 1l4 3 4-3z"/></svg>
        <span>youremail@mail.com</span>
      </li>
      <li>
        <svg viewBox="0 0 12 12"><path d="M6 0a6 6 0 1 0 0 12A6 6 0 0 0 6 0zM1.5 5.3h9v1.4h-9z"/></svg>
        <span>www.yourwebsite.com</span>
      </li>
    </ul>
    <div class="name-band">
      <div class="person">
        <div class="person-name">your name</div>
        <div class="person-title">designation</div>
      </div>
    </div>
  </section>
</body>
</html>
```